Wed site for biomedical device startup

We need a generic website for a medical device startup. I will provide examples below of websites from other companies that can serve as models for what we are looking for. The startup is for a device that can non invasively measure blood flow in the brain using light. The application is to detect the type of stroke someone is having before they get to the hospital so treatment can be started right away. This saves patients upto hours of delayed treatment. Patients will be able to recover from stroke much better and faster as a result. I have attached an AI generated illustration of what the device will ultimately look like for reference.

https://www.872vantora.com
https://quilvesta.com

Target Market(s)

Biomedical, medical device, investors of biomedical device startups

Industry/Entity Type

Biomedical

Coding

Coded - Design and coding required

Number of Pages Required

4 page

Requirements
Must have
• same section and section headings as example websites listed above
Nice to have
• similar to example websites listed above. Prefer a darker website over a lighter one. Perhaps dark blues to go with logo colors. A moving background image element at top of landing page could be cool. Something indicative of heartbeat, or neurons, or blood flow.

```html
<!DOCTYPE html>
<html lang="en">
<head>
<meta charset="utf-8">
<title>LUMVERA — Revolutionizing Stroke Diagnosis</title>
<link rel="stylesheet" href="https://fonts.googleapis.com/css2?family=Orbitron:wght@500;600;700;800;900&family=Poppins:wght@300;400;500;600&display=swap">
<style>
  :root{
    --navy:#0b0a3d;
    --navy-deep:#08072e;
    --ink:#0f0e35;
    --purple:#8a2be2;
    --violet:#7b3fe4;
    --cyan:#19d3e6;
    --muted:#555a6e;
    --soft:#f3f5fb;
    --white:#ffffff;
    --grad:linear-gradient(90deg,#9b27d9 0%,#5a66e8 50%,#19d6e8 100%);
    --head:'Orbitron',sans-serif;
    --body:'Poppins',sans-serif;
  }
  *{box-sizing:border-box;margin:0;padding:0}
  html,body{width:1200px;height:3157px;overflow:hidden}
  body{position:relative;background:var(--white);font-family:var(--body);color:var(--ink)}
  .abs{position:absolute}

  .bg-wash{left:0;top:0;width:1200px;height:1850px;
    background:
      radial-gradient(ellipse 520px 460px at 1000px 60px,#eef0f8 0%,rgba(238,240,248,0) 70%),
      radial-gradient(ellipse 700px 600px at 120px 1300px,#f1f3f9 0%,rgba(241,243,249,0) 70%),
      radial-gradient(ellipse 600px 500px at 1150px 800px,#f0f2f9 0%,rgba(240,242,249,0) 70%);}

  /* header */
  .brand{display:flex;align-items:center;gap:12px;font-family:var(--head);font-weight:500;letter-spacing:2px;color:var(--ink)}
  .brand-dot{border-radius:50%;background:var(--violet)}
  .site-header .brand{left:88px;top:24px;font-size:36px}
  .site-header .brand-dot{width:56px;height:56px}
  .nav{left:613px;top:40px;display:flex;gap:40px;font-family:var(--head);font-weight:600;font-size:16px;letter-spacing:.5px}
  .nav a{color:var(--ink);text-decoration:none}

  /* hero */
  .hero-kicker{left:86px;top:290px;font-family:var(--head);font-weight:800;font-size:39px;letter-spacing:1px}
  .hero-title{left:84px;top:336px;font-family:var(--head);font-weight:900;font-size:84px;letter-spacing:2px;
    background:var(--grad);-webkit-background-clip:text;background-clip:text;color:transparent}
  .hero-sub{left:86px;top:421px;font-family:var(--head);font-weight:800;font-size:39px;letter-spacing:1px}
  .hero-lead{left:89px;top:477px;width:430px;font-size:15px;line-height:22px;color:var(--muted)}
  .photo-lab{left:591px;top:123px;width:352px;height:571px;border-radius:176px;
    background:linear-gradient(160deg,#c9d3e4 0%,#e9eef6 40%,#7d93c4 75%,#3c58b8 100%);box-shadow:0 20px 40px rgba(20,30,80,.12)}
  .photo-lab-2{left:965px;top:88px;width:300px;height:415px;border-radius:150px;
    background:linear-gradient(160deg,#a9bedb 0%,#dfe6f1 45%,#6f86be 100%)}

  /* intro row */
  .video-thumb{left:96px;top:744px;width:204px;height:159px;border-radius:80px;
    background:linear-gradient(150deg,#7fa0c2 0%,#d5dfea 50%,#5a7cb8 100%)}
  .play{left:243px;top:745px;width:57px;height:57px;border-radius:50%;background:var(--violet);display:flex;align-items:center;justify-content:center}
  .intro-text{left:347px;top:774px;font-family:var(--head);font-weight:600;font-size:22px;line-height:33px;letter-spacing:.5px}
  .impact-photo{left:883px;top:756px;width:98px;height:136px;border-radius:68px;
    background:linear-gradient(150deg,#9bb3d4,#e4e9f1 60%,#7489b8)}
  .impact-badge{left:964px;top:755px;width:138px;height:138px;border-radius:50%;
    background:linear-gradient(135deg,#6c3ce0,#4a5ee8)}

  /* feature panel */
  .panel{left:86px;top:1099px;width:1022px;height:495px;border-radius:150px 150px 150px 150px;background:var(--navy)}
  .panel-photo{left:178px;top:981px;width:394px;height:570px;border-radius:197px 197px 190px 190px;
    background:linear-gradient(170deg,#2d6db0 0%,#7aa9d6 30%,#c48aa8 65%,#5a3f8a 100%)}
  .panel-title{left:624px;top:1198px;font-family:var(--head);font-weight:700;font-size:29px;line-height:36px;color:var(--white);letter-spacing:.5px}
  .panel-list{left:624px;top:1294px;width:420px;list-style:none;color:#e6e8f5;font-size:14px;line-height:22px}
  .panel-list li{position:relative;padding-left:18px;margin-bottom:15px}
  .panel-list li::before{content:"";position:absolute;left:0;top:8px;width:7px;height:7px;border-radius:50%;background:#5a7ef0}
  .btn-grad{left:624px;top:1460px;width:151px;height:46px;border-radius:23px;background:var(--grad);color:var(--white);
    font-family:var(--body);font-weight:600;font-size:13px;display:flex;align-items:center;justify-content:center}

  /* technology */
  .eyebrow{left:0;width:1200px;text-align:center;top:1678px;font-family:var(--head);font-weight:600;font-size:18px;letter-spacing:1px;
    background:var(--grad);-webkit-background-clip:text;background-clip:text;color:transparent}
  .section-title{left:0;width:1200px;text-align:center;top:1710px;font-family:var(--head);font-weight:800;font-size:29px;letter-spacing:1px}
  .card{top:1771px;width:276px;height:239px;background:var(--white);border-radius:14px;box-shadow:0 14px 40px rgba(40,50,110,.08);text-align:center;padding-top:35px}
  .card svg{display:block;margin:0 auto}
  .card h3{margin-top:24px;font-family:var(--head);font-weight:600;font-size:14px;letter-spacing:.5px}
  .card p{margin:10px auto 0;width:232px;font-size:13px;line-height:20px;color:var(--muted)}

  /* how we help */
  .help-kicker{left:148px;top:2183px;font-family:var(--head);font-weight:700;font-size:25px;letter-spacing:1px}
  .help-title{left:146px;top:2220px;font-family:var(--head);font-weight:900;font-size:43px;letter-spacing:1px;
    background:var(--grad);-webkit-background-clip:text;background-clip:text;color:transparent}
  .help-copy{left:148px;top:2284px;width:468px;font-size:15px;line-height:24px;color:var(--muted)}
  .anatomy{left:672px;top:2092px;width:394px;height:480px;border-radius:190px 190px 0 0;
    background:linear-gradient(180deg,#1c67b8 0%,#2a8ad6 45%,#1a4ea8 100%)}

  /* footer */
  .footer{left:0;top:2565px;width:1200px;height:592px;background:var(--navy-deep);border-radius:70px 70px 0 0}
  .cta{left:25px;top:2589px;width:1150px;height:236px;border-radius:110px;background:var(--grad);text-align:center;color:var(--white)}
  .cta h2{margin-top:40px;font-family:var(--head);font-weight:900;font-size:55px;letter-spacing:2px}
  .cta p{margin:14px auto 0;width:800px;font-size:19px;line-height:25px;color:#f1ecff}
  .btn-light{left:500px;top:2793px;width:198px;height:62px;border-radius:31px;background:var(--white);border:5px solid var(--navy-deep);
    font-weight:600;font-size:16px;color:var(--ink);display:flex;align-items:center;justify-content:center}
  .foot-col{top:2932px;width:160px;text-align:center;color:#aeb2cf;font-size:14px;line-height:27px}
  .foot-col h4{font-family:var(--head);font-weight:700;font-size:16px;color:var(--white);letter-spacing:1px;margin-bottom:8px}
  .footer-brand{left:0;width:1200px;top:2926px;justify-content:center;font-size:54px;color:var(--white)}
  .footer-brand .brand-dot{width:80px;height:80px}
  .foot-mail{left:0;width:1200px;top:3002px;text-align:center;font-size:14px;color:#aeb2cf}
  .rule{left:70px;top:3107px;width:1060px;height:1px;background:#2c2c66}
  .to-top{left:1130px;top:3088px;width:36px;height:36px;border-radius:50%;background:var(--violet);display:flex;align-items:center;justify-content:center}
  .copyright{left:0;width:1200px;top:3125px;text-align:center;font-size:13px;color:#aeb2cf}
</style>
</head>
<body>
  <div class="abs bg-wash"></div>

  <header class="site-header">
    <div class="abs brand"><span class="brand-dot"></span>LUMVERA</div>
    <nav class="abs nav"><a href="#">About</a><a href="#">Technology</a><a href="#">Publications</a><a href="#">Contact</a></nav>
  </header>

  <section class="hero">
    <div class="abs hero-kicker">REVOLUTIONIZING</div>
    <div class="abs hero-title">STROKE</div>
    <div class="abs hero-sub">DIAGNOSIS</div>
    <p class="abs hero-lead">Detect Stroke type before hospital arrival, saving valuable time and improving outcomes.</p>
    <div class="abs photo-lab" role="img" aria-label="Scientist in a lab coat looking into a microscope"></div>
    <div class="abs photo-lab-2" role="img" aria-label="Researcher working at a microscope in a laboratory"></div>
  </section>

  <section class="intro">
    <div class="abs video-thumb" role="img" aria-label="Video still of a researcher working in a lab"></div>
    <div class="abs play"><svg width="20" height="22" viewBox="0 0 20 22"><path d="M3 2 L18 11 L3 20 Z" fill="#fff"/></svg></div>
    <div class="abs intro-text">VENTRICULAR HEMORRHAGE<br>IS A DEVASTATING RISK FOR VERY<br>PREMATURE INFANTS.</div>
    <div class="abs impact-photo" role="img" aria-label="Researcher wearing safety glasses"></div>
    <div class="abs impact-badge">
      <svg width="138" height="138" viewBox="0 0 138 138">
        <defs><path id="ring" d="M69,69 m-50,0 a50,50 0 1,1 100,0 a50,50 0 1,1 -100,0"/></defs>
        <text font-family="Poppins, sans-serif" font-size="12.5" fill="#fff" letter-spacing="1.2"><textPath href="#ring">Discover the Impact • Discover the Impact •</textPath></text>
        <path d="M48 69 H90 M76 55 L90 69 L76 83" stroke="#fff" stroke-width="4" fill="none" stroke-linecap="round" stroke-linejoin="round"/>
      </svg>
    </div>
  </section>

  <section class="feature">
    <div class="abs panel"></div>
    <div class="abs panel-photo" role="img" aria-label="Patient wearing a light-based sensor on the forehead beside a handheld monitor"></div>
    <h2 class="abs panel-title">Portable. Light-based.<br>Life-saving.</h2>
    <ul class="abs panel-list">
      <li>Our device uses safe, non-invasive light technology to measure brain blood flow.</li>
      <li>It detects the type of stroke in minutes, even before the patient arrives at the hospital.</li>
      <li>This allows for immediate, life-saving treatment decisions.</li>
    </ul>
    <a class="abs btn-grad">LEARN MORE</a>
  </section>

  <section class="technology">
    <div class="abs eyebrow">ADVANCED TECHNOLOGY</div>
    <h2 class="abs section-title">INNOVATIVE BLOOD LOSS MONITORING</h2>
    <article class="abs card" style="left:174px">
      <svg width="60" height="70" viewBox="0 0 60 70" fill="none" stroke="#5a5ee6" stroke-width="2.5">
        <rect x="4" y="3" width="52" height="64" rx="8"/><rect x="12" y="11" width="36" height="24" rx="3"/>
        <path d="M15 24 H22 L25 17 L29 30 L33 20 L36 24 H45"/><circle cx="18" cy="50" r="4"/><circle cx="30" cy="50" r="4"/><circle cx="42" cy="50" r="4"/>
      </svg>
      <h3>PORTABLE MONITORING</h3>
      <p>Compact, wearable devices that provide continuous blood loss monitoring anywhere, anytime.</p>
    </article>
    <article class="abs card" style="left:462px">
      <svg width="70" height="70" viewBox="0 0 70 70" fill="none" stroke="#5a5ee6" stroke-width="2.5">
        <circle cx="35" cy="35" r="31"/><circle cx="35" cy="35" r="23" stroke-dasharray="3 4"/>
        <path d="M24 36 L32 44 L47 27" stroke-width="4" stroke-linecap="round" stroke-linejoin="round"/>
      </svg>
      <h3>REAL-TIME ALERTS</h3>
      <p>Instant notifications to caregivers when critical thresholds are reached.</p>
    </article>
    <article class="abs card" style="left:750px">
      <svg width="70" height="70" viewBox="0 0 70 70" fill="none" stroke="#5a5ee6" stroke-width="2.5">
        <circle cx="30" cy="18" r="12"/><path d="M6 66 V54 Q6 40 22 38 H38"/><circle cx="50" cy="54" r="11"/><path d="M50 48 V60 M44 54 H56"/>
      </svg>
      <h3>PATIENT-CENTERED</h3>
      <p>Easy-to-use interface designed for both patients and healthcare providers</p>
    </article>
  </section>

  <section class="help">
    <div class="abs help-kicker">WHO IT HELPS</div>
    <h2 class="abs help-title">HOW WE HELP</h2>
    <p class="abs help-copy">It is a long established fact that a reader will be distracted by the readable content of a page when looking at its layout. The point of using Lorem Ipsum is that it has a more-or-less normal distribution of letters, as opposed to using 'Content here, content here', making it look like readable English. Many desktop publishing packages and web page editors now use Lorem Ipsum as their default model text, and a search for 'lorem ipsum' will uncover many web sites still in their infancy.</p>
    <div class="abs anatomy" role="img" aria-label="Anatomical illustration of a human torso showing the heart and blood vessels"></div>
  </section>

  <footer>
    <div class="abs footer"></div>
    <div class="abs cta">
      <h2>STAY CONNECTED</h2>
      <p>Join our community to receive updates about our latest developments and research in blood loss monitoring technology.</p>
    </div>
    <a class="abs btn-light">GET IN TOUCH</a>
    <div class="abs foot-col" style="left:137px"><h4>COMPANY</h4>About<br>Press</div>
    <div class="abs brand footer-brand"><span class="brand-dot"></span>LUMVERA</div>
    <div class="abs foot-mail">info@lumvera.com</div>
    <div class="abs foot-col" style="left:886px"><h4>LEGAL</h4>Privacy Policy<br>Terms of Service</div>
    <div class="abs rule"></div>
    <div class="abs to-top"><svg width="12" height="8" viewBox="0 0 12 8"><path d="M2 6 L6 2 L10 6" stroke="#fff" stroke-width="2" fill="none"/></svg></div>
    <div class="abs copyright">2025 LUMVERA. All rights reserved.</div>
  </footer>
</body>
</html>
```